Label Redesign For Hemp Oil Tincture Bottle*

I need a label redesigned for Marbleleaf Hemp, current bottle label and logo is attached. The current label doesn't standout, not sure if its the font size or colors on the existing label. It is very important to have on the label that this is a Premium Full Spectrum Hemp Oil that is 2000mg. Then after the label is redesigned and approved, I would need to packaging to be designed to match the approved label design.
This Hemp oil has a relaxing effect to help ease mental and emotional stress, tension and worry. The Omega Fatty Acids it contains also naturally improves your mood and overall brain function, causing you to feel more alert and focused. Hemp Oil helps with insomnia. Take some 2-3 hours before bedtime, you will feel relaxed yet aware of how tired you are that it will lead to a good night's sleep. Hemp Oil helps ease chronic pain and inflammation from conditions such as arthritis, fibromyalgia, lupus, and MS. As a pain relief supplement, it is a safer, natural, non-chemical and non-addictive alternative to prescription painkillers.

Target Market(s)

Adults

Industry/Entity Type

Supplement

Font styles to use
Serif
Sans Serif

Colors

Designer to choose colors to be used in the design.

Requirements
Must have
• All information thats on current label but where it says 750 in the front of the existing label, it needs to say 2000. The 2000 should be prominent on the label.

```html
<!DOCTYPE html>
<html lang="en">
<head>
<meta charset="utf-8">
<title>Marbleleaf Hemp Premium – Label</title>
<link href="https://fonts.googleapis.com/css2?family=Oswald:wght@500&family=Montserrat:ital,wght@0,600;0,700;1,800&family=Great+Vibes&display=swap" rel="stylesheet">
<style>
  :root{
    --page:#e3e5e7;
    --paper:#eef0f1;
    --teal:#49adba;
    --teal-text:#2fa2b2;
    --deep-teal:#2c6d79;
    --lavender:#c6c8e4;
    --stripe:#5b69bd;
    --leaf-green:#b9d29a;
    --leaf-grey:#8c8f92;
    --white:#ffffff;
  }
  *{margin:0;padding:0;box-sizing:border-box}
  html,body{width:1200px;height:1200px;overflow:hidden;background:var(--page)}
  .label{position:absolute;left:390px;top:25px;width:420px;height:1150px;background:var(--paper);overflow:hidden;font-family:"Montserrat",sans-serif}
  .label-shapes{position:absolute;inset:0}
  .leaf-mark{position:absolute;left:324px;top:318px;width:96px;height:240px;border-radius:48% 0 0 48%;background:linear-gradient(160deg,var(--leaf-green),var(--leaf-grey) 70%);opacity:.85}
  .label-text{position:absolute;left:16px;line-height:1;white-space:nowrap;z-index:1}
  .thc-claim{left:94px;top:88px;font-family:"Oswald",sans-serif;font-weight:500;font-size:37px;color:var(--deep-teal);letter-spacing:.5px}
  .brand-name{top:221px;font-family:"Oswald",sans-serif;font-weight:500;font-size:46px;color:var(--deep-teal)}
  .product-name{top:263px;font-weight:700;font-size:92px;color:var(--deep-teal);letter-spacing:.5px}
  .grade{top:352px;font-family:"Oswald",sans-serif;font-weight:500;font-size:58px;color:var(--deep-teal)}
  .spectrum{left:22px;top:511px;font-weight:600;font-size:36px;color:var(--teal-text)}
  .strength{left:22px;top:560px;font-weight:600;font-size:31px;color:var(--teal-text)}
  .supplement{top:657px;font-weight:800;font-style:italic;font-size:41px;color:var(--white);line-height:47px}
  .benefits{top:753px;font-weight:600;font-size:30px;color:var(--white);line-height:38px}
  .flavor-note{top:868px;font-family:"Great Vibes",cursive;font-size:52px;color:var(--white)}
  .flavor{top:931px;font-weight:600;font-size:32px;color:var(--white)}
  .volume{position:absolute;left:221px;top:1053px;width:189px;height:97px;background:var(--deep-teal);border-radius:16px 16px 0 0;padding:14px 14px 0 0;text-align:right;font-family:"Oswald",sans-serif;font-weight:500;font-size:34px;line-height:36px;color:var(--white);z-index:1}
  .base-band{position:absolute;left:0;right:0;bottom:0;height:27px;background:var(--deep-teal)}
</style>
</head>
<body>
  <main class="label">
    <svg class="label-shapes" width="420" height="1150" viewBox="0 0 420 1150" aria-hidden="true">
      <path d="M0 0 H352 C300 120 160 195 0 197 Z" fill="var(--lavender)"/>
      <path d="M0 62 C45 35 105 12 150 0 H118 C75 12 35 28 0 44 Z" fill="var(--stripe)"/>
      <path d="M0 92 C60 55 130 25 190 0 H170 C110 22 50 50 0 78 Z" fill="var(--white)"/>
      <path d="M0 620 C130 640 300 600 420 531 V1150 H0 Z" fill="var(--teal)"/>
    </svg>

    <div class="leaf-mark" role="img" aria-label="Hemp leaf illustration"></div>

    <div class="label-text thc-claim">ZERO THC</div>
    <div class="label-text brand-name">MARBLELEAF</div>
    <div class="label-text product-name">HEMP</div>
    <div class="label-text grade">PREMIUM</div>

    <div class="label-text spectrum">Full Spectrum</div>
    <div class="label-text strength">2000 Hemp Oil</div>

    <div class="label-text supplement">DIETARY<br>SUPPLEMENT</div>
    <div class="label-text benefits">pain,sleeplessness<br>anxiety &amp; inflammation</div>

    <div class="label-text flavor-note">Natural</div>
    <div class="label-text flavor">Peppermint Flavor</div>

    <div class="base-band"></div>
    <div class="volume">1FL.OZ<br>(30ML)</div>
  </main>
</body>
</html>
```